IT Company Business Card design

Brisk Node is a new computer solutions business focusing on setting up servers and computer systems for small to medium sized businesses.

A business client will either request a solution, or support for a current system and we will turn up on site to provide these services.

We are bast in Christchurch, New Zealand.

We are looking for unique business card's that stand out and show off the business in a professional light.

Open to all idea's etc.

Industry/Entity Type

Computer

Requirements
Must have
• Business Logo (AI file attached)
Employee Name
Business title
Business landline number
Cell phone number
Email
Web URL
Nice to have
• Could be nice to have some keywords (possibly on the back) such as:

Business IT solutions
Network installations
Phone solutions
Server management
Software diagnostics

The above is not needed, just an idea.

```html
<!DOCTYPE html>
<html lang="en">
<head>
<meta charset="utf-8">
<title>Brisk Node — Business Card</title>
<link rel="stylesheet" href="https://fonts.googleapis.com/css2?family=Encode+Sans+Condensed:wght@400;500;600&family=Raleway:wght@300&family=Open+Sans:wght@400;700&display=swap">
<style>
  :root {
    --backdrop: #d9dadc;
    --card-white: #ffffff;
    --navy: #1f2a63;
    --sky: #1aa3e0;
    --sky-deep: #0b84c4;
    --sky-light: #33b6ea;
    --ink-grey: #6b6e73;
    --rule-grey: #8c8f94;
    --logo-grey: #3a3d42;
  }
  * { box-sizing: border-box; margin: 0; padding: 0; }
  html, body { width: 1200px; height: 960px; overflow: hidden; }
  body {
    background: var(--backdrop);
    display: flex;
    flex-direction: column;
    align-items: center;
    justify-content: center;
    gap: 44px;
  }
  .card {
    width: 720px;
    height: 410px;
    border-radius: 38px;
    position: relative;
    overflow: hidden;
    box-shadow: 0 10px 30px rgba(0,0,0,0.18);
  }

  /* Front */
  .card-front { background: var(--card-white); }
  .brand {
    position: absolute; left: 58px; top: 58px;
    display: flex; align-items: center; gap: 22px;
  }
  .brand-mark {
    width: 86px; height: 86px; border-radius: 50%;
    background: linear-gradient(135deg, var(--sky-light), var(--navy));
  }
  .brand-divider { width: 2px; height: 96px; background: linear-gradient(var(--card-white), #b5b8bc, var(--card-white)); }
  .brand-name {
    font-family: "Raleway", sans-serif; font-weight: 300;
    font-size: 36px; letter-spacing: 4px; color: var(--logo-grey);
  }
  .person { position: absolute; right: 50px; top: 170px; text-align: right; }
  .person-name {
    font-family: "Encode Sans Condensed", sans-serif; font-weight: 600;
    font-size: 30px; color: var(--navy);
  }
  .person-title {
    font-family: "Encode Sans Condensed", sans-serif; font-weight: 400;
    font-size: 22px; color: var(--sky); margin-top: 6px;
  }
  .name-rule {
    position: absolute; left: 58px; right: 50px; top: 210px; height: 2px;
    background: linear-gradient(90deg, rgba(140,143,148,0), var(--rule-grey) 70%, rgba(140,143,148,0.2));
  }
  .contact {
    position: absolute; left: 58px; bottom: 46px;
    font-family: "Encode Sans Condensed", sans-serif; font-size: 22px; color: var(--ink-grey);
    display: flex; flex-direction: column; gap: 10px;
  }
  .contact-row { display: flex; align-items: center; gap: 10px; }
  .contact-sep { width: 2px; height: 24px; background: var(--ink-grey); margin: 0 4px; }
  .contact-icon { width: 20px; height: 20px; flex: none; }
  .contact-web { color: var(--sky); font-weight: 500; }

  /* Back */
  .card-back {
    background: radial-gradient(ellipse at 75% 35%, #48c0ee, var(--sky) 45%, var(--sky-deep));
  }
  .back-disc {
    position: absolute; right: 70px; top: 40px;
    width: 300px; height: 300px; border-radius: 50%;
    background: rgba(255,255,255,0.22);
    display: flex; align-items: center; justify-content: center;
  }
  .back-url {
    font-family: "Open Sans", sans-serif; font-size: 20px;
    letter-spacing: 1.5px; color: var(--card-white);
  }
  .back-url strong { font-weight: 700; }
  .back-social {
    position: absolute; left: 58px; bottom: 44px;
    display: flex; align-items: center; gap: 10px;
    font-family: "Open Sans", sans-serif; font-size: 18px;
    letter-spacing: 1px; color: var(--card-white);
  }
  .back-social-dot { width: 22px; height: 22px; border-radius: 50%; background: var(--card-white); }
</style>
</head>
<body>

  <section class="card card-front" aria-label="Business card front">
    <div class="brand">
      <div class="brand-mark"></div>
      <div class="brand-divider"></div>
      <div class="brand-name">BRISK NODE</div>
    </div>

    <div class="person">
      <div class="person-name">Mara Ellison</div>
      <div class="person-title">Director</div>
    </div>
    <div class="name-rule"></div>

    <div class="contact">
      <div class="contact-row">BRISK NODE, 14 Kent Lane, Christchurch</div>
      <div class="contact-row">
        <svg class="contact-icon" viewBox="0 0 20 20" aria-hidden="true">
          <circle cx="10" cy="10" r="10" fill="#1aa3e0"/>
          <path d="M7 5c1 0 1.6 2 1.2 2.8L7.6 8.6c.6 1.6 1.8 2.9 3.4 3.6l.8-.7c.8-.4 2.8.3 2.8 1.2 0 1-1 2.3-2.2 2.2C8.6 14.6 5.3 11.4 5 7.5 4.9 6.2 6 5 7 5z" fill="#fff"/>
        </svg>
        <span>03-555-0148</span>
        <span class="contact-sep"></span>
        <svg class="contact-icon" viewBox="0 0 20 20" aria-hidden="true">
          <rect x="5" y="1" width="10" height="18" rx="2" fill="#1aa3e0"/>
          <rect x="7" y="4" width="6" height="9" fill="#fff"/>
          <circle cx="10" cy="16" r="1.2" fill="#fff"/>
        </svg>
        <span>021-555-0273</span>
      </div>
      <div class="contact-row">
        <svg class="contact-icon" viewBox="0 0 20 20" aria-hidden="true">
          <rect x="1" y="4" width="18" height="13" rx="1.5" fill="#1aa3e0"/>
          <path d="M1.5 5l8.5 6.5L18.5 5" fill="none" stroke="#fff" stroke-width="1.6"/>
        </svg>
        <span>info@brisknode.nz</span>
        <span class="contact-sep"></span>
        <span class="contact-web">www.brisknode.nz</span>
      </div>
    </div>
  </section>

  <section class="card card-back" aria-label="Business card back">
    <div class="back-disc">
      <div class="back-url">www.<strong>brisknode</strong>.nz</div>
    </div>
    <div class="back-social">
      <span class="back-social-dot"></span>
      <span>/brisknode</span>
    </div>
  </section>

</body>
</html>
```